K48 PowerPoint Presentation

As you can see the design of this PowerPoint isn't cohesive. There are a lot of images and words that give it a very jumbled and busy appeal. We want to turn this into a sharp, cohesive and visually appealing presentation without taking away too much of the information. Feel free to use the images to create your own artwork for the PowerPoint.

Please don't hesitate to contact me with any questions.

Industry/Entity Type

Graphic Design

```html
<!DOCTYPE html>
<html lang="en">
<head>
<meta charset="utf-8">
<title>Idea to Reality</title>
<link rel="stylesheet" href="https://fonts.googleapis.com/css2?family=Carlito:wght@400;700&display=swap">
<style>
  :root {
    --band: #efefef;
    --title: #1f3f6e;
    --navy: #1b3a6b;
    --teal: #3f7f99;
    --deep: #1d5487;
    --arrow: #c4c4c4;
    --white: #ffffff;
  }
  * { margin: 0; padding: 0; box-sizing: border-box; }
  html, body { width: 1200px; height: 750px; overflow: hidden; background: var(--white); }
  body { font-family: "Carlito", "Calibri", sans-serif; position: relative; }
  .header-band { position: absolute; left: 0; top: 0; width: 1200px; height: 100px; background: var(--band); }
  .slide-title { position: absolute; left: 78px; top: 28px; font-size: 42px; font-weight: 400; color: var(--title); }
  .brand-mark { position: absolute; right: 24px; top: 26px; display: flex; align-items: center; gap: 8px; }
  .brand-dot { width: 30px; height: 30px; border-radius: 50%; background: var(--title); }
  .brand-name { font-size: 28px; font-weight: 700; color: var(--title); }
  .tagline { position: absolute; left: 200px; top: 198px; width: 440px; text-align: center; font-size: 25px; font-weight: 700; color: var(--navy); line-height: 1.35; }
  .app-view { position: absolute; border: 1px solid #8a8a8a; box-shadow: 2px 3px 6px rgba(0,0,0,.25); }
  .view-back { left: 923px; top: 247px; width: 226px; height: 167px; background: linear-gradient(180deg, #f4f4f4 0 30%, #3f6aa8 30% 100%); }
  .view-mid { left: 825px; top: 190px; width: 238px; height: 160px; background: linear-gradient(90deg, #d8e3ef 0 35%, #f6c9d6 35% 70%, #f1f3f7 70% 100%); }
  .view-front { left: 718px; top: 118px; width: 233px; height: 155px; background: linear-gradient(180deg, #d9d9d9 0 12%, #c9a58a 12% 55%, #d6b060 55% 100%); }
  .step { position: absolute; top: 433px; width: 242px; height: 200px; padding: 14px 10px; color: var(--white); }
  .step-challenge { left: 120px; background: var(--teal); }
  .step-need { left: 458px; background: var(--teal); }
  .step-result { left: 796px; background: var(--deep); }
  .step h2 { font-size: 23px; font-weight: 700; margin-bottom: 6px; }
  .step p { font-size: 18px; line-height: 1.3; }
  .flow-arrows { position: absolute; left: 0; top: 0; }
  .footer-mark { position: absolute; left: 18px; top: 690px; display: flex; align-items: center; gap: 8px; }
  .footer-dot { width: 36px; height: 36px; border-radius: 50%; background: var(--title); }
  .footer-name { font-size: 34px; font-weight: 700; color: var(--title); }
</style>
</head>
<body>
  <div class="header-band"></div>
  <h1 class="slide-title">Idea to Reality</h1>
  <div class="brand-mark"><span class="brand-dot"></span><span class="brand-name">Orbitline</span></div>

  <div class="tagline">A Web-Based Environment for Architecture Decision Analytics</div>

  <div class="app-view view-back" role="img" aria-label="Application screen with a bar and line chart"></div>
  <div class="app-view view-mid" role="img" aria-label="Application screen with a table, pie chart and bar chart"></div>
  <div class="app-view view-front" role="img" aria-label="Application screen with maps of systems by state"></div>

  <svg class="flow-arrows" width="1200" height="750" viewBox="0 0 1200 750" aria-hidden="true">
    <defs>
      <marker id="head" markerWidth="6" markerHeight="6" refX="3" refY="3" orient="auto">
        <path d="M0,0 L6,3 L0,6 Z" fill="#c4c4c4"/>
      </marker>
    </defs>
    <path d="M302,646 Q400,700 508,655" fill="none" stroke="#c4c4c4" stroke-width="7" marker-end="url(#head)"/>
    <path d="M652,405 Q750,345 852,403" fill="none" stroke="#c4c4c4" stroke-width="7" marker-start="url(#head)" marker-end="url(#head)"/>
  </svg>

  <section class="step step-challenge">
    <h2>The Challenge</h2>
    <p>Identifying / integrating An organizations “sources of record” information and making it readily available (assets, budget, systems, references).</p>
  </section>
  <section class="step step-need">
    <h2>The Need</h2>
    <p>A portal solution enabling the rapid ingestion, organization, integration, display and analysis of data from multiple sources.</p>
  </section>
  <section class="step step-result">
    <h2>The Result</h2>
    <p>A collaborative architecture decision support tool that allows users to associate mission guidance with mission execution</p>
  </section>

  <div class="footer-mark"><span class="footer-dot"></span><span class="footer-name">K48</span></div>
</body>
</html>
```